Silver Brook Decorators Banner

Create a banner that displays and reinforces Silver Brook Decorators’ brand identity while promoting our interior painting services. The banner will be displayed at indoor venues through the winter. The design should be clean, professional, and visually recognizable to both new and returning customers. See attached design brief & logo source files.

```html
<!DOCTYPE html>
<html lang="en">
<head>
<meta charset="utf-8">
<title>Silver Brook Decorators Banner</title>
<link href="https://fonts.googleapis.com/css2?family=Poppins:wght@400;500;600;700;800&display=swap" rel="stylesheet">
<style>
  :root {
    --stage: #3f4641;
    --green: #7a9f5c;
    --green-dark: #4f7a3e;
    --brand: #6e9a55;
    --band: #4b524d;
    --ink: #2f3430;
    --rule: #c9ccc9;
    --white: #ffffff;
  }
  * { margin: 0; padding: 0; box-sizing: border-box; }
  html, body { width: 1200px; height: 574px; overflow: hidden; background: var(--stage); font-family: "Poppins", sans-serif; }
  .banner { position: absolute; left: 0; top: 47px; width: 1200px; height: 480px; overflow: hidden; background: var(--white); }
  .hero { position: absolute; left: 0; top: 0; width: 1200px; height: 295px; background: linear-gradient(90deg, #7aa25c 0%, #739a57 55%, #4e7b3e 100%); }
  .hero-photo { position: absolute; right: 0; top: 0; width: 490px; height: 295px;
    background: radial-gradient(ellipse at 70% 70%, #c9e07a 0%, #8fcf8a 35%, #4ea66a 60%, rgba(78,123,62,0) 80%); }
  .headline { position: absolute; left: 50px; top: 24px; color: var(--white); font-weight: 800; font-size: 134px; line-height: 1; letter-spacing: -3px; text-shadow: 0 3px 8px rgba(0,0,0,.25); white-space: nowrap; }
  .subhead { position: absolute; left: 54px; top: 151px; width: 592px; height: 70px; background: var(--green-dark); color: var(--white); font-weight: 600; font-size: 60px; line-height: 70px; padding-left: 14px; text-shadow: 0 2px 6px rgba(0,0,0,.25); white-space: nowrap; }
  .tagline { position: absolute; left: 54px; top: 230px; color: var(--ink); font-size: 31px; font-weight: 400; white-space: nowrap; }
  .services { position: absolute; left: 0; top: 295px; width: 1200px; height: 54px; background: var(--band); color: var(--white); font-weight: 600; font-size: 35px; line-height: 54px; text-align: right; padding-right: 42px; white-space: nowrap; }
  .services .dot { display: inline-block; width: 9px; height: 9px; border-radius: 50%; background: var(--brand); margin: 0 15px; vertical-align: middle; }
  .brand-name { position: absolute; left: 48px; top: 366px; color: var(--brand); font-weight: 700; font-size: 50px; line-height: 46px; letter-spacing: -0.5px; white-space: nowrap; }
  .estimate { position: absolute; left: 500px; top: 392px; white-space: nowrap; }
  .label { color: var(--brand); font-weight: 500; font-size: 20px; line-height: 26px; }
  .url { color: var(--ink); font-size: 26px; font-weight: 400; line-height: 38px; margin-top: 2px; }
  .url b { font-weight: 700; }
  .divider { position: absolute; left: 846px; top: 393px; width: 1px; height: 62px; background: var(--rule); }
  .contact { position: absolute; left: 873px; top: 392px; white-space: nowrap; }
  .phone { display: flex; align-items: center; gap: 14px; margin-top: 2px; color: var(--ink); font-weight: 600; font-size: 29px; line-height: 38px; }
  .phone svg { width: 31px; height: 31px; flex: none; }
</style>
</head>
<body>
  <div class="banner">
    <div class="hero">
      <div class="hero-photo" role="img" aria-label="Fanned green paint colour swatches with a wooden paint brush"></div>
      <div class="headline">INTERIOR</div>
      <div class="subhead">PAINTING SERVICES</div>
      <div class="tagline">Trusted local professionals, since 2005</div>
    </div>
    <div class="services">WALLS<span class="dot"></span>CEILINGS<span class="dot"></span>TRIM<span class="dot"></span>CABINETS<span class="dot"></span>DRYWALL REPAIR</div>
    <div class="brand-name">SILVER BROOK<br>DECORATORS</div>
    <div class="estimate">
      <div class="label">Book a Free Estimate at</div>
      <div class="url">www.<b>sbdecorators</b>.com</div>
    </div>
    <div class="divider"></div>
    <div class="contact">
      <div class="label">Contact us at</div>
      <div class="phone">
        <svg viewBox="0 0 32 32" aria-hidden="true">
          <circle cx="16" cy="16" r="16" fill="#6e9a55"/>
          <path d="M11.5 8.5l2.4 3.6-1.6 1.7c.9 2.2 2.7 4 4.9 4.9l1.7-1.6 3.6 2.4-1.2 3c-6.4-.2-11.4-5.2-11.6-11.6z" fill="#2f3430"/>
        </svg>
        <span>+1 802-555-0148</span>
      </div>
    </div>
  </div>
</body>
</html>
```